Design for Flavored drink product

I need a packaging design for flavoured drinks product.
The product is a flavoured drink product.

There will be various flavours i.e. orange, apple, strawberry, etc.
However, you may design the product using one sample flavour first (i.e. orange), as the designs of other flavours could be adjusted afterwards.

The temporary product name is: ZOBLIX

The measurement is 20,2 cm (Length) x 12,8 cm (Height).

The target customers are young audiences (10 years - 35 years old).

I want the product design to be something 'fun' and 'colourful'.
The design concept could be anything depends on your imagination.
Basically, I want you to be creative in designing the logo and the overall graphic design for the label.

I am hoping to have a product design that can stand out in the supermarket shelf.
It must be eye catchy and attractive.

- Create something different. Something extraordinary -

Note: You may refer to design sample attached

Thank you and Good Luck!

Thank you,
Marcus

```html
<!DOCTYPE html>
<html lang="en">
<head>
<meta charset="utf-8">
<title>ZOBLIX flavoured drink labels</title>
<link rel="stylesheet" href="https://fonts.googleapis.com/css2?family=Fredoka:wght@600&family=Gochi+Hand&display=swap">
<style>
  :root {
    --backdrop-light: #f7f7f8;
    --backdrop-dark: #dcdcde;
    --label-dark: #3b3b3d;
    --brand-orange: #ee5a12;
    --apple-green: #93c94a;
    --orange-fruit: #ee6a14;
    --lemon-yellow: #f7c51e;
    --ink-white: #ffffff;
  }
  * { box-sizing: border-box; margin: 0; padding: 0; }
  html, body { width: 1200px; height: 857px; overflow: hidden; }
  body {
    background: radial-gradient(ellipse at 40% 40%, var(--backdrop-light) 0%, var(--backdrop-dark) 100%);
    position: relative;
    font-family: "Fredoka", sans-serif;
  }
  .label {
    position: absolute;
    top: 170px;
    width: 230px;
    height: 560px;
    background: var(--label-dark);
    border-radius: 28px;
    overflow: hidden;
  }
  .label--apple { left: 40px; }
  .label--orange { left: 300px; top: 220px; }
  .label--lemon { left: 560px; top: 150px; }

  .label__brand {
    position: absolute;
    top: 48px; left: 0; right: 0;
    text-align: center;
    color: var(--brand-orange);
    font-size: 44px;
    font-weight: 600;
    letter-spacing: 1px;
  }
  .label__brand sup {
    font-size: 12px;
    vertical-align: top;
    margin-left: 2px;
  }
  .label__band {
    position: absolute;
    top: 130px; left: 0;
    width: 230px; height: 100px;
  }
  .label__flavour {
    position: absolute;
    top: 150px; left: 0; right: 0;
    text-align: center;
    color: var(--ink-white);
    font-size: 34px;
    font-weight: 600;
  }
  .label__fruit {
    position: absolute;
    top: 260px; left: 18px;
    width: 194px; height: 210px;
    border-radius: 50% 50% 46% 46%;
  }
  .label--apple .label__fruit { background: var(--apple-green); }
  .label--orange .label__fruit { background: var(--orange-fruit); }
  .label--lemon .label__fruit { background: var(--lemon-yellow); }

  .label__claim {
    position: absolute;
    top: 305px; left: 60px;
    color: var(--ink-white);
    font-family: "Gochi Hand", cursive;
    font-size: 30px;
    line-height: 1.05;
  }

  .brand-mark {
    position: absolute;
    left: 800px; top: 385px;
    width: 330px;
    display: flex;
    align-items: center;
    gap: 14px;
  }
  .brand-mark__dot {
    width: 22px; height: 22px;
    border-radius: 50%;
    background: var(--apple-green);
  }
  .brand-mark__name {
    color: var(--brand-orange);
    font-size: 78px;
    font-weight: 600;
    letter-spacing: 2px;
  }
  .brand-mark__tm {
    align-self: flex-start;
    color: var(--brand-orange);
    font-size: 16px;
    font-weight: 600;
    margin-left: -8px;
    margin-top: 8px;
  }
</style>
</head>
<body>

  <section class="label label--apple">
    <div class="label__brand">ZOBLIX<sup>TM</sup></div>
    <svg class="label__band" viewBox="0 0 230 100" aria-hidden="true">
      <path d="M0 10 Q115 -10 230 10 Q180 95 115 95 Q50 95 0 10 Z" fill="var(--brand-orange)"/>
    </svg>
    <div class="label__flavour">apple</div>
    <div class="label__fruit" role="img" aria-label="Illustrated green apple"></div>
    <p class="label__claim">100%<br>natural<br>flavor</p>
  </section>

  <section class="label label--orange">
    <div class="label__brand">ZOBLIX<sup>TM</sup></div>
    <svg class="label__band" viewBox="0 0 230 100" aria-hidden="true">
      <path d="M0 10 Q115 -10 230 10 Q180 95 115 95 Q50 95 0 10 Z" fill="var(--brand-orange)"/>
    </svg>
    <div class="label__flavour">Orange</div>
    <div class="label__fruit" role="img" aria-label="Illustrated orange fruit"></div>
    <p class="label__claim">100%<br>natural<br>flavor</p>
  </section>

  <section class="label label--lemon">
    <div class="label__brand">ZOBLIX<sup>TM</sup></div>
    <svg class="label__band" viewBox="0 0 230 100" aria-hidden="true">
      <path d="M0 10 Q115 -10 230 10 Q180 95 115 95 Q50 95 0 10 Z" fill="var(--brand-orange)"/>
    </svg>
    <div class="label__flavour">lemon</div>
    <div class="label__fruit" role="img" aria-label="Illustrated yellow lemon"></div>
    <p class="label__claim">100%<br>natural<br>flavor</p>
  </section>

  <div class="brand-mark">
    <span class="brand-mark__dot"></span>
    <span class="brand-mark__name">ZOBLIX</span>
    <span class="brand-mark__tm">TM</span>
  </div>

</body>
</html>
```